Freshen up Product Labels

We need product label designs refreshed throughout our brand. We will start with the main product as that will set the basic design for most other labels. We are currently using 2.5" wide x 4.5" tall vinyl labels for most products and would like to stick to that size for this project. There are 3 of this size label on a jug of our all natural house cleaning concentrate. Uploaded current design and open to your new ideas. Our products can be found in more detail at quillbrook.com

```html
<!DOCTYPE html>
<html lang="en">
<head>
<meta charset="utf-8">
<title>Quillbrook Aromatherapy Cleaning Concentrate Label</title>
<link href="https://fonts.googleapis.com/css2?family=Montserrat:wght@400;500;700;800&display=swap" rel="stylesheet">
<style>
  :root {
    --plum: #5a1646;
    --maroon-dark: #6e2236;
    --maroon: #a3394f;
    --paper: #ffffff;
    --stage: #ffffff;
    --icon-light: #ffffff;
    --icon-grey: #cfcfd3;
    --text-font: "Montserrat", Arial, sans-serif;
  }
  * { box-sizing: border-box; margin: 0; padding: 0; }
  html, body { width: 1200px; height: 860px; overflow: hidden; background: var(--stage); }
  body { position: relative; font-family: var(--text-font); color: var(--plum); }

  .label {
    position: absolute; left: 378px; top: 30px; width: 444px; height: 800px;
    background: var(--paper);
    box-shadow: 10px 14px 22px rgba(0,0,0,0.28);
  }
  .brand-band {
    position: absolute; left: 115px; top: 0; width: 213px; height: 175px;
    background: linear-gradient(180deg, var(--maroon-dark), var(--maroon));
  }
  .brand-badge {
    position: absolute; left: 114px; top: 66px; width: 216px; height: 216px;
    border-radius: 50%; background: var(--paper);
    border: 5px solid var(--maroon-dark);
    display: flex; align-items: center; justify-content: center;
  }
  .brand-name {
    font-weight: 800; font-size: 27px; letter-spacing: 0.5px; color: var(--plum);
  }
  .product-title {
    position: absolute; left: 0; top: 290px; width: 100%;
    text-align: center; font-weight: 700; font-size: 38px; line-height: 37px;
    letter-spacing: 0.2px;
  }
  .oils-banner {
    position: absolute; left: 18px; top: 420px; width: 407px; height: 35px;
    background: linear-gradient(90deg, var(--maroon-dark), var(--maroon));
    color: #fff; font-weight: 700; font-size: 21px;
    display: flex; align-items: center; justify-content: center;
  }
  .oil {
    position: absolute; width: 118px; height: 90px;
  }
  .oil-icon {
    position: absolute; left: 17px; top: 0; width: 84px; height: 84px; border-radius: 50%;
    background: radial-gradient(circle at 50% 35%, var(--icon-light) 35%, var(--icon-grey) 100%);
  }
  .oil-name {
    position: absolute; left: 0; top: 52px; width: 118px; height: 24px;
    background: linear-gradient(90deg, var(--maroon-dark), var(--maroon));
    color: #fff; font-size: 18px; font-weight: 400; line-height: 24px; text-align: center;
  }
  .rule {
    position: absolute; left: 89px; width: 274px; height: 1.5px;
    background: linear-gradient(90deg, transparent, var(--maroon) 20%, var(--maroon) 80%, transparent);
  }
  .formula {
    position: absolute; left: 0; top: 684px; width: 100%; text-align: center;
    font-weight: 600; font-size: 20.5px;
  }
  .volume {
    position: absolute; left: 0; top: 731px; width: 100%; text-align: center;
    font-weight: 800; font-size: 22px;
  }
  .yield {
    position: absolute; left: 0; top: 762px; width: 100%; text-align: center;
    font-weight: 400; font-size: 18.5px;
  }
</style>
</head>
<body>
  <section class="label">
    <div class="brand-band"></div>
    <div class="brand-badge"><span class="brand-name">QUILLBROOK</span></div>

    <h1 class="product-title">Aromatherapy<br>Cleaning<br>Concentrate</h1>

    <div class="oils-banner">Contains Powerful Essential Oils</div>

    <div class="oil" style="left:30px; top:471px;"><div class="oil-icon" role="img" aria-label="Cinnamon sticks icon"></div><div class="oil-name">Cinnamon</div></div>
    <div class="oil" style="left:163px; top:471px;"><div class="oil-icon" role="img" aria-label="Clove buds icon"></div><div class="oil-name">Clove</div></div>
    <div class="oil" style="left:296px; top:471px;"><div class="oil-icon" role="img" aria-label="Lemon slice icon"></div><div class="oil-name">Lemon</div></div>
    <div class="oil" style="left:30px; top:574px;"><div class="oil-icon" role="img" aria-label="Rosemary sprig icon"></div><div class="oil-name">Rosemary</div></div>
    <div class="oil" style="left:163px; top:574px;"><div class="oil-icon" role="img" aria-label="Peppermint leaf icon"></div><div class="oil-name">Peppermint</div></div>
    <div class="oil" style="left:296px; top:574px;"><div class="oil-icon" role="img" aria-label="Eucalyptus branch icon"></div><div class="oil-name">Eucalyptus</div></div>

    <div class="rule" style="top:678px;"></div>
    <p class="formula">Ultra-Concentrated Versatile Formula</p>
    <div class="rule" style="top:718px;"></div>
    <p class="volume">64 oz</p>
    <p class="yield">Makes up to 24 Gallons of Cleaner</p>
  </section>
</body>
</html>
```